International Food Manufacturer in the need of a new business card and logo.

Our Company - Northgate Pantry Ltd.

Our Industry - Food and Drink

We are a Wild Harvested Food Distributor / Manufacturer. We service the following food sectors: Supermarkets, Hotels, Restaurants, Cafes, Catering and all people looking to eat healthy food products.

Slogan - Wild-harvested goodness for every kitchen

Business card details -

48-52 Marlow Lane
Hatherby Green
London
EC9Z 4RT United Kingdom
Dennis Prowle
+44 7000 481736 - UK
+971 50 7739205 - UAE
+38 063 914 2758 - Ukraine
dennis@northgatepantry.example
www.northgatepantry.example

Goal - We are looking for a dynamic modern new look for our corporate image and a designer who can bring this new concept to our future food product designs. Please try to incorporate 3d hexagonal vector Imaging in your design concepts.

Target Market(s)

Industry/Entity Type

Food Service

Contact Information for Business Card

Northgate Pantry Ltd.
48-52 Marlow Lane
Hatherby Green
London
EC9Z 4RT United Kingdom
Dennis Prowle
+44 7000 481736 - UK
+971 50 7739205 - UAE

Font styles to use
Serif

Colors

Designer to choose colors to be used in the design.

Requirements
Must have
• Please read project description above.
Nice to have
Should not have

```html
<!DOCTYPE html>
<html lang="en">
<head>
<meta charset="utf-8">
<title>Northgate Pantry Ltd. – Business Card</title>
<link rel="stylesheet" href="https://fonts.googleapis.com/css2?family=Encode+Sans+Condensed:wght@200;300;400;700&display=swap">
<style>
  :root {
    --olive: #5b6b2e;
    --olive-dark: #4d5e22;
    --olive-text: #5d6b35;
    --paper: #ffffff;
  }
  html, body {
    margin: 0;
    padding: 0;
    width: 1200px;
    height: 720px;
    overflow: hidden;
    background: var(--olive);
  }
  .card {
    position: relative;
    width: 1200px;
    height: 720px;
    background: var(--olive);
    font-family: "Encode Sans Condensed", "Arial Narrow", sans-serif;
  }
  .card__panel {
    position: absolute;
    left: 27px;
    top: 27px;
    width: 1146px;
    height: 663px;
    background: var(--paper);
  }
  .card__badge {
    position: absolute;
    left: 0;
    top: 0;
    width: 1200px;
    height: 720px;
  }
  .brand {
    position: absolute;
    left: 133px;
    top: 381px;
    margin: 0;
    color: var(--paper);
    font-weight: 400;
    font-size: 30px;
    line-height: 44px;
  }
  .brand__mark {
    position: absolute;
    left: 176px;
    top: 262px;
    width: 64px;
    height: 64px;
    border-radius: 50%;
    background: var(--paper);
  }
  .contact {
    position: absolute;
    left: 649px;
    top: 127px;
    color: var(--olive-text);
    font-weight: 300;
    font-size: 31px;
    line-height: 39.3px;
  }
  .contact__name {
    margin: 0 0 36px;
    color: var(--olive-dark);
    font-weight: 700;
    font-size: 33px;
    line-height: 44px;
  }
  .contact__address,
  .contact__lines {
    margin: 0;
    font-style: normal;
  }
  .contact__address {
    margin-bottom: 32px;
  }
  .tagline {
    position: absolute;
    right: 75px;
    top: 644px;
    margin: 0;
    color: var(--olive-dark);
    font-weight: 700;
    font-size: 30px;
    line-height: 40px;
  }
</style>
</head>
<body>
  <div class="card">
    <div class="card__panel"></div>

    <svg class="card__badge" viewBox="0 0 1200 720" aria-hidden="true">
      <path fill="var(--olive)" d="M27 74 H255 Q298 74 319 108 L462 333 Q478 358 462 383 L319 611 Q298 645 255 645 H27 Z"/>
    </svg>

    <span class="brand__mark" aria-hidden="true"></span>
    <p class="brand">Northgate<br>Pantry Ltd.</p>

    <div class="contact">
      <h1 class="contact__name">Dennis Prowle</h1>
      <address class="contact__address">
        48-52 Marlow Lane<br>
        Hatherby Green<br>
        London<br>
        EC9Z 4RT United Kingdom
      </address>
      <p class="contact__lines">
        +44 7000 481736 - UK<br>
        +971 50 7739205 - UAE<br>
        +38 063 914 2758 - Ukraine<br>
        dennis@northgatepantry.example<br>
        www.northgatepantry.example
      </p>
    </div>

    <p class="tagline">Wild-harvested goodness for every kitchen</p>
  </div>
</body>
</html>
```